Business Card Design Project

Business Card
We are rebranding with a new logo
Industry/Entity Type
Business
Contact Information for Business Card
Doug Farrow +61 457820913 doug@lumora.com.au P.O. Box 728 Kelmscott QLD 4309
Requirements
Must have
- Logo

```html
<!DOCTYPE html>
<html lang="en">
<head>
<meta charset="utf-8">
<title>Lumora International – Business Card</title>
<link rel="stylesheet" href="https://fonts.googleapis.com/css2?family=Roboto:wght@400;500;700&family=Roboto+Condensed:wght@700&display=swap">
<style>
  :root {
    --backdrop: #1d1d1f;
    --card-white: #f4f4f4;
    --blue-light: #0aa2dc;
    --blue-mid: #0a6f97;
    --blue-dark: #0a4a66;
    --swoosh: #0d5676;
    --brand-blue: #0b6f98;
    --text-light: #ffffff;
  }
  * { margin: 0; padding: 0; box-sizing: border-box; }
  html, body {
    width: 1200px; height: 960px; overflow: hidden;
    background: var(--backdrop);
    font-family: "Roboto", Arial, sans-serif;
  }
  .card {
    position: absolute; left: 407px; top: 143px;
    width: 386px; height: 674px;
    border-radius: 20px; overflow: hidden;
    background: var(--card-white);
  }
  .card-art { position: absolute; inset: 0; width: 386px; height: 674px; }
  .brand {
    position: absolute; left: 0; right: 0; top: 92px;
    display: flex; align-items: center; justify-content: center; gap: 14px;
    color: var(--brand-blue); font-weight: 500;
  }
  .brand-dot { width: 30px; height: 30px; border-radius: 50%; background: var(--brand-blue); }
  .brand-name { font-size: 46px; line-height: 1; letter-spacing: 1px; }
  .brand-name small { display: block; font-size: 17px; letter-spacing: 4px; margin-top: 8px; }
  .contact {
    position: absolute; right: 56px; top: 449px;
    text-align: right; color: var(--text-light);
  }
  .contact-name {
    font-family: "Roboto Condensed", "Arial Narrow", sans-serif;
    font-weight: 700; font-size: 23px; letter-spacing: 0.3px; margin-bottom: 17px;
  }
  .contact-address { font-size: 15.5px; line-height: 20px; margin-bottom: 15px; }
  .contact-lines { list-style: none; font-size: 15.5px; line-height: 21.5px; margin-right: -2px; }
  .contact-lines li { display: flex; justify-content: flex-end; align-items: center; gap: 9px; }
  .contact-lines svg { width: 14px; height: 14px; fill: var(--text-light); }
</style>
</head>
<body>
  <article class="card">
    <svg class="card-art" viewBox="0 0 386 674" aria-hidden="true">
      <defs>
        <radialGradient id="blueGlow" cx="200" cy="470" r="260" gradientUnits="userSpaceOnUse">
          <stop offset="0" stop-color="var(--blue-light)"/>
          <stop offset="0.55" stop-color="var(--blue-mid)"/>
          <stop offset="1" stop-color="var(--blue-dark)"/>
        </radialGradient>
      </defs>
      <path class="blue-field" d="M0,600 C80,440 210,300 386,272 L386,674 L0,674 Z" fill="url(#blueGlow)"/>
      <path class="swoosh" d="M4,560 C90,410 220,300 386,270 C240,292 110,400 4,560 Z" fill="var(--swoosh)"/>
      <path class="swoosh" d="M22,520 C110,380 230,295 370,275 C240,300 120,385 22,520 Z" fill="var(--swoosh)"/>
    </svg>

    <div class="brand">
      <span class="brand-dot"></span>
      <span class="brand-name">Lumora<small>INTERNATIONAL</small></span>
    </div>

    <div class="contact">
      <p class="contact-name">DOUG FARROW</p>
      <p class="contact-address">P.O. Box 728<br>Kelmscott QLD 4309</p>
      <ul class="contact-lines">
        <li>+61 457820913
          <svg viewBox="0 0 24 24"><path d="M6.6 10.8a15.1 15.1 0 0 0 6.6 6.6l2.2-2.2a1 1 0 0 1 1-.25 11.4 11.4 0 0 0 3.6.57 1 1 0 0 1 1 1V20a1 1 0 0 1-1 1A17 17 0 0 1 3 4a1 1 0 0 1 1-1h3.5a1 1 0 0 1 1 1c0 1.25.2 2.45.57 3.57a1 1 0 0 1-.25 1Z"/></svg>
        </li>
        <li>doug@lumora.com.au
          <svg viewBox="0 0 24 24"><path d="M2 5h20v14H2Z M3 6l9 7 9-7" fill="none" stroke="#fff" stroke-width="2"/><path d="M2 5h20L12 12Z"/></svg>
        </li>
        <li>www.lumora.com.au
          <svg viewBox="0 0 24 24"><circle cx="12" cy="12" r="10"/><path d="M8 6c2 1 1 3 3 4s-1 3 1 5-1 3-1 3M15 5c-1 2 2 3 3 5" fill="none" stroke="var(--blue-mid)" stroke-width="2"/></svg>
        </li>
      </ul>
    </div>
  </article>
</body>
</html>
```